Ironvale Shift Services

We are a underground coal mining labour hire company, needing a website that links into our online payroll (www.wagetrakker.com.au) and also need to have job applications page that is a preform with drop down menu,s with answers or check boxes. We would also need a 3 tier administration access for access to different files.
We are looking for an ongoing relationship with future app integration

Reason: There are a few more designs to come and I'm out at the mine for another week

Industry/Entity Type

Coal Mining

```html
<!DOCTYPE html>
<html lang="en">
<head>
<meta charset="utf-8">
<title>Ironvale Shift Services</title>
<link href="https://fonts.googleapis.com/css2?family=PT+Sans:wght@400;700&display=swap" rel="stylesheet">
<style>
  :root {
    --black: #000000;
    --logo-bg: #0b0b0b;
    --white: #ffffff;
    --orange: #f7891f;
    --orange-light: #f9b522;
    --text-dark: #1a1a1a;
    --text-grey: #666666;
    --panel-left: #f5f5f5;
    --panel-right: #e6e6e6;
    --field-border: #d0d0d0;
    --btn-grey: #c9c9c9;
    --btn-grey-text: #8a8a8a;
    --dot: #5a5a5a;
    --dot-active: #cfcfcf;
  }
  * { box-sizing: border-box; margin: 0; padding: 0; }
  html, body { width: 1200px; height: 1153px; overflow: hidden; }
  body { font-family: "PT Sans", sans-serif; background: var(--white); position: relative; }

  .site-header { position: absolute; left: 0; top: 0; width: 1200px; height: 116px; background: var(--black); }
  .brand { position: absolute; left: 14px; top: 12px; width: 188px; height: 90px; background: var(--logo-bg); display: flex; align-items: center; gap: 8px; padding-left: 10px; }
  .brand-mark { flex: none; width: 66px; height: 66px; border: 3px solid var(--white); border-radius: 50%; }
  .brand-name { color: var(--white); font-size: 26px; font-weight: 400; white-space: nowrap; }
  .main-nav a { position: absolute; top: 51px; color: var(--white); font-size: 12.5px; text-decoration: none; text-transform: uppercase; white-space: nowrap; }
  .main-nav a.is-active { color: var(--orange); }
  .main-nav .has-sub::after { content: ""; position: absolute; left: 50%; top: 22px; margin-left: -5px; border-left: 5px solid transparent; border-right: 5px solid transparent; border-top: 5px solid var(--white); }

  .hero { position: absolute; left: 0; top: 116px; width: 1200px; height: 450px; background: radial-gradient(ellipse at 55% 30%, #5a5a5a 0%, #333 40%, #1c1c1c 75%, #111 100%); }
  .hero-title { position: absolute; left: 64px; top: 111px; font-size: 28.5px; line-height: 33px; font-weight: 400; color: var(--white); }
  .hero-title span { display: block; color: var(--orange); }
  .hero-copy { position: absolute; left: 66px; top: 204px; width: 578px; color: var(--white); font-size: 10.5px; line-height: 15.6px; text-align: justify; }
  .hero-copy p + p { margin-top: 15.6px; }
  .btn-more { position: absolute; display: flex; align-items: center; justify-content: center; font-size: 12px; text-decoration: none; }
  .hero .btn-more { left: 573px; top: 365px; width: 71px; height: 24px; background: var(--orange); color: var(--white); }
  .slider-dots { position: absolute; left: 1066px; top: 390px; display: flex; gap: 9px; }
  .slider-dots i { width: 8px; height: 8px; background: var(--dot); display: block; }
  .slider-dots i:first-child { background: var(--dot-active); }

  .quick-links { position: absolute; left: 0; top: 566px; width: 1200px; height: 204px; background: radial-gradient(ellipse 260px 90px at 200px 0, var(--orange-light), transparent), radial-gradient(ellipse 260px 90px at 600px 0, var(--orange-light), transparent), radial-gradient(ellipse 260px 90px at 1000px 0, var(--orange-light), transparent), var(--orange); }
  .quick-link { position: absolute; top: 64px; width: 200px; margin-left: -100px; text-align: center; color: var(--white); text-decoration: none; font-size: 21px; line-height: 24px; text-transform: uppercase; }
  .quick-link svg { display: block; margin: 0 auto 22px; height: 40px; }

  .welcome { position: absolute; left: 0; top: 770px; width: 795px; height: 383px; background: var(--panel-left); }
  .signup { position: absolute; left: 795px; top: 770px; width: 405px; height: 383px; background: var(--panel-right); }
  .section-title { position: absolute; top: 50px; font-size: 28.5px; font-weight: 400; color: var(--text-dark); }
  .welcome .section-title { left: 64px; }
  .welcome-copy { position: absolute; left: 64px; top: 121px; width: 668px; font-size: 14.2px; line-height: 16.6px; color: var(--text-dark); text-align: justify; }
  .welcome-copy p + p { margin-top: 16px; }
  .signup .section-title { left: 51px; }
  .signup-intro { position: absolute; left: 52px; top: 120px; width: 293px; font-size: 10.6px; line-height: 12.6px; color: var(--text-grey); text-align: justify; word-spacing: 0.6px; }
  .field { position: absolute; left: 50px; width: 294px; height: 29px; background: var(--white); border: 1px solid var(--field-border); font: 10.5px "PT Sans", sans-serif; padding-left: 14px; color: var(--text-dark); }
  .field-email { top: 185px; }
  .field-contact { top: 227px; height: 28px; }
  .signup .btn-more { left: 274px; top: 276px; width: 71px; height: 24px; background: var(--btn-grey); color: var(--btn-grey-text); }
</style>
</head>
<body>
  <header class="site-header">
    <div class="brand"><span class="brand-mark"></span><span class="brand-name">Ironvale</span></div>
    <nav class="main-nav">
      <a href="#" class="is-active" style="left:579px">Home</a>
      <a href="#" style="left:653px">About Us</a>
      <a href="#" class="has-sub" style="left:758px">Vision</a>
      <a href="#" class="has-sub" style="left:839px">Employer Services</a>
      <a href="#" style="left:1004px">Team</a>
      <a href="#" style="left:1080px">Contact</a>
    </nav>
  </header>

  <section class="hero" role="img" aria-label="Dark close-up photograph of coal lumps">
    <h1 class="hero-title">The Best Labour Solutions<span>Independent Thinking</span></h1>
    <div class="hero-copy">
      <p>Nulla ac mi dapibus, fermentum augue in, dapibus sapien. Donec sit amet eros eget lectus aliquam tincidunt a ultricies lacus. Morbi aliquet scelerisque nibh sed tempor. Etiam sed consequat leo. Quisque et nibh in mauris sagittis fermentum. Suspendisse fermentum quam eget dolor porttitor varius. Nulla scelerisque felis at ultrices hendrerit.</p>
      <p>Phasellus vitae ultricies ante, sit amet dignissim nulla. Fusce a diam nec massa faucibus bibendum eu ac mi. Curabitur eleifend nulla in libero cursus, sed pellentesque tellus lobortis. Donec tincidunt accumsan massa ac rh aliquet scelerisque nibh sed tempor. Etiam sed consequat leo. Quisque et nibh in mauris sagittis fermentum. Suspendisse fermentum quam eget dolor porttitor varius. Nulla scelerisque felis at ultrices hendrerit.</p>
    </div>
    <a href="#" class="btn-more">more</a>
    <div class="slider-dots"><i></i><i></i><i></i><i></i><i></i></div>
  </section>

  <section class="quick-links">
    <a href="#" class="quick-link" style="left:213px">
      <svg viewBox="0 0 28 40" width="28" fill="#fff"><circle cx="14" cy="10" r="9"/><path d="M3 40 V28 Q3 20 9 19 L14 24 L19 19 Q25 20 25 28 V40 Z"/></svg>Register</a>
    <a href="#" class="quick-link" style="left:590px">
      <svg viewBox="0 0 30 40" width="30"><circle cx="12" cy="14" r="8.5" fill="none" stroke="#fff" stroke-width="4"/><path d="M18 21 L27 32" stroke="#fff" stroke-width="6" stroke-linecap="round"/></svg>Find Work</a>
    <a href="#" class="quick-link" style="left:980px">
      <svg viewBox="0 0 38 40" width="38" fill="#fff"><path d="M13 10 V5 H25 V10" fill="none" stroke="#fff" stroke-width="3"/><rect x="0" y="10" width="38" height="26" rx="2"/></svg>Find Jobs</a>
  </section>

  <section class="welcome">
    <h2 class="section-title">Welcome To Ironvale</h2>
    <div class="welcome-copy">
      <p>Nulla ac mi dapibus, fermentum augue in, dapibus sapien. Donec sit amet eros eget lectus aliquam tincidunt a ultricies lacus. Morbi aliquet scelerisque nibh sed tempor. Etiam sed consequat leo. Quisque et nibh in mauris sagittis fermentum. Suspendisse fermentum quam eget dolor porttitor varius. Nulla scelerisque felis at ultrices hendrerit.</p>
      <p>Phasellus vitae ultricies ante, sit amet dignissim nulla. Fusce a diam nec massa faucibus bibendum eu ac mi. Curabitur eleifend nulla in libero cursus, sed pellentesque tellus lobortis. Donec tincidunt accumsan massa ac rh aliquet scelerisque nibh sed tempor. Etiam sed consequat leo. Quisque et nibh in mauris sagittis fermentum. Suspendisse fermentum quam eget dolor porttitor varius. Nulla scelerisque felis at ultrices hendrerit.</p>
    </div>
  </section>

  <section class="signup">
    <h2 class="section-title">Signup for Ironvale</h2>
    <p class="signup-intro">ulla ac mi dapibus, fermentum augue in, dapibus sapien. Donec sit amet eros eget lectus aliquam tincidunt a ultricies lacus. Morbi aliquet scelerisque nibh sed tempor.</p>
    <input class="field field-email" type="text" placeholder="Email">
    <input class="field field-contact" type="text" placeholder="Contact">
    <a href="#" class="btn-more">more</a>
  </section>
</body>
</html>
```